We are an integrated facilities management company.

We aggregate everything related to facilities maintenance. Repair-replacement of equipment and facility space materials from:
Asset gathering and tracking.
Vendor screening, contracting and management.
Service requirement development.
Work order processing and management.
Invoice reconciliation.
Vendor payment.
Reporting.
Capital equipment bids and project management.

Target Market(s)

Retail, hospitality, multi-family housing, long term healthcare.

Industry/Entity Type

Maintenance

Contact Information for Business Card

Professional and bold look. (see logo zip file)

Colors
3377b5
85abd2
cedeed

Requirements
Must have
• N/A
Nice to have
• N/A
Should not have
• N/A

```html
<!DOCTYPE html>
<html lang="en">
<head>
<meta charset="utf-8">
<title>Keystone Facility Partners — Business Card</title>
<link href="https://fonts.googleapis.com/css2?family=Work+Sans:wght@400;600;700&family=Tinos:wght@700&display=swap" rel="stylesheet">
<style>
  :root {
    --backdrop: #c9c9c9;
    --card-white: #ffffff;
    --brand-blue: #2a78b9;
    --name-blue: #2a74b6;
    --rule-blue: #85abd2;
    --link-blue: #6a9fd3;
    --ink: #3a3a3a;
    --mark-steel: #3f5f7c;
    --card-radius: 24px;
  }
  * { box-sizing: border-box; margin: 0; padding: 0; }
  html, body {
    width: 1125px; height: 1200px; overflow: hidden;
    background: var(--backdrop);
    font-family: "Work Sans", Arial, sans-serif;
    color: var(--ink);
  }
  .canvas { position: relative; width: 1125px; height: 1200px; }
  .card {
    position: absolute; left: 178px; width: 768px; height: 436px;
    border-radius: var(--card-radius);
  }
  .card--front { top: 140px; background: var(--card-white); }
  .card--back { top: 626px; background: var(--brand-blue); }

  .brand {
    position: absolute; display: flex; align-items: center; gap: 10px;
    font-family: "Work Sans", Arial, sans-serif; font-weight: 700;
    color: var(--mark-steel); white-space: nowrap;
  }
  .brand__square { background: var(--mark-steel); flex: none; }
  .card--front .brand { right: 43px; top: 68px; font-size: 22px; }
  .card--front .brand__square { width: 22px; height: 22px; }
  .card--back .brand {
    left: 0; right: 0; top: 196px; justify-content: center;
    font-size: 38px; gap: 16px;
  }
  .card--back .brand__square { width: 38px; height: 38px; }

  .person { position: absolute; left: 39px; top: 203px; }
  .person__name {
    font-family: "Tinos", "Times New Roman", serif; font-weight: 700;
    font-size: 30px; letter-spacing: 2px; color: var(--name-blue); line-height: 1;
  }
  .person__role { font-size: 18px; margin-top: 12px; }

  .divider {
    position: absolute; left: 39px; right: 40px; top: 295px;
    height: 2px; background: var(--rule-blue);
  }

  .contact { position: absolute; left: 39px; top: 314px; list-style: none; }
  .contact li {
    display: flex; align-items: center; gap: 9px;
    font-size: 18px; height: 31px;
  }
  .contact svg { width: 13px; height: 13px; fill: var(--name-blue); flex: none; }
  .contact__domain { color: var(--link-blue); }

  .address {
    position: absolute; right: 40px; top: 353px;
    text-align: right; font-size: 18px; line-height: 23px; font-style: normal;
  }
</style>
</head>
<body>
<main class="canvas">
  <section class="card card--front">
    <div class="brand"><span class="brand__square"></span>Keystone Facility Partners</div>

    <div class="person">
      <h1 class="person__name">Marcus Hale</h1>
      <p class="person__role">Doctor</p>
    </div>

    <div class="divider"></div>

    <ul class="contact">
      <li>
        <svg viewBox="0 0 24 24" aria-hidden="true"><path d="M6.6 10.8a15.1 15.1 0 0 0 6.6 6.6l2.2-2.2a1 1 0 0 1 1-.25 11.4 11.4 0 0 0 3.6.57 1 1 0 0 1 1 1V20a1 1 0 0 1-1 1A17 17 0 0 1 3 4a1 1 0 0 1 1-1h3.5a1 1 0 0 1 1 1c0 1.25.2 2.45.57 3.57a1 1 0 0 1-.25 1z"/></svg>
        410-555-0187
      </li>
      <li>
        <svg viewBox="0 0 24 24" aria-hidden="true"><path d="M2 4h20v16H2zm2 2v.5l8 5 8-5V6zm0 3v9h16V9l-8 5z"/></svg>
        hello@keystonefm.com
      </li>
      <li>
        <svg viewBox="0 0 24 24" aria-hidden="true"><path d="M12 2a10 10 0 1 0 0 20 10 10 0 0 0 0-20zm-1 17.9A8 8 0 0 1 4.2 10.3L9 15v1a2 2 0 0 0 2 2zm6.9-2.5A2 2 0 0 0 16 16h-1v-3a1 1 0 0 0-1-1H8v-2h2a1 1 0 0 0 1-1V7h2a2 2 0 0 0 2-2v-.4a8 8 0 0 1 2.9 12.8z"/></svg>
        <span>www.<span class="contact__domain">keystonefm</span>.com</span>
      </li>
    </ul>

    <address class="address">Street Address 4100<br>Harbor Falls Maryland 21090</address>
  </section>

  <section class="card card--back">
    <div class="brand"><span class="brand__square"></span>Keystone Facility Partners</div>
  </section>
</main>
</body>
</html>
```